GUARANTEED! Simple website for independent event planner and consultant...

I need a website that is no more than 5 or 6 pages to illustrate who I am and what I can offer to groups who book hotels for meetings and conferences. I have 20 years of experience planning meetings within hotels and I am now ready to go out on my own and help clients choose venues, negotiate contracts and plan effective meetings. I will focus on clients planning meetings in the mountains of Colorado but I am willing to travel as well. I want to work with a person who is collaborative and can direct me on what they need to move the project along quickly. I already have my logo, a hosting site and work e-mail address. Also, I recently hired a photographer to do head shots. Lastly, it important for me to be able to talk on the phone or skype with this person, as needed and I must be able to make changes to my site down the road when necessary...

Target Market(s)

Corporate Groups

Industry/Entity Type

Event Planning

Coding

Coded - Design and coding required

Number of Pages Required

5+ page

Font styles to use
Sans Serif

Requirements
Must have
• About me page, event planning services offered page, task force and consulting work page, testimonials page, page for blogs, page to contact me/request a proposal. May need advice on what else I need...
Nice to have
• I want it to look sharp and professional. I want people to look at my site and know immediately that they can trust me and the work I can do.
• I don't want it to look like it is over the top as I am not a HUGE company but I do want it to be professional and easy to view and navigate.
Should not have
• Bright colors
• My logo is bright orange and black. I have also used dark grey and orange. See below:
• Orange:
• C = 0
• M = 64
• Y = 100
• K = 0
• Gray:
• C = 67
• M = 60
• Y = 59
• K = 45
• Font: Gotham Book and Gotham Bold

```html
<!DOCTYPE html>
<html lang="en">
<head>
<meta charset="utf-8">
<title>About – Halden Event Management</title>
<link href="https://fonts.googleapis.com/css2?family=Montserrat:wght@400;500;700&family=Raleway:wght@400;500&display=swap" rel="stylesheet">
<style>
  :root {
    --orange: #f47920;
    --ink: #1e1e1e;
    --text: #3a3a3a;
    --rule: #f3a66c;
    --panel: #f7f7f7;
    --white: #ffffff;
    --border: #e6e6e6;
  }
  * { box-sizing: border-box; margin: 0; padding: 0; }
  html, body { width: 1200px; height: 612px; overflow: hidden; background: var(--white); }
  .page { position: relative; width: 1200px; height: 612px; overflow: hidden; font-family: "Raleway", Arial, sans-serif; color: var(--text); }

  .sidebar { position: absolute; left: 0; top: 0; width: 248px; height: 612px; background: var(--white); }
  .brand-name { position: absolute; left: 28px; top: 62px; font-family: "Montserrat", Arial, sans-serif; font-weight: 500; color: var(--ink); font-size: 14px; line-height: 18px; letter-spacing: 0.2px; white-space: nowrap; }

  .main-nav { position: absolute; left: 26px; top: 164px; width: 154px; list-style: none; }
  .main-nav li { padding-bottom: 6px; margin-bottom: 9px; border-bottom: 1px solid var(--rule); }
  .main-nav li:last-child { border-bottom: none; margin-bottom: 0; }
  .nav-title { display: block; font-family: "Montserrat", Arial, sans-serif; font-weight: 500; font-size: 13.5px; color: var(--ink); line-height: 17px; letter-spacing: 0.2px; }
  .nav-sub { display: block; font-size: 9.5px; color: var(--ink); line-height: 13px; }

  .social-bar { position: absolute; left: 0; top: 494px; width: 225px; height: 43px; background: var(--orange); }
  .social-dot { position: absolute; top: 16px; width: 11px; height: 11px; border-radius: 50%; background: var(--white); }

  .hero { position: absolute; left: 248px; top: 0; width: 952px; height: 356px;
    background: linear-gradient(100deg, #e4e4e4 0%, #b9b9b9 22%, #6e6e6e 38%, #3b3d40 55%, #2b2e32 75%, #3d4246 100%); }
  .hero-title { position: absolute; left: 483px; top: 160px; }
  .hero-title h1 { font-family: "Montserrat", Arial, sans-serif; font-weight: 700; font-size: 37px; color: var(--orange); line-height: 40px; }
  .hero-title p { font-family: "Montserrat", Arial, sans-serif; font-weight: 400; font-size: 17.5px; color: var(--white); letter-spacing: 0.4px; line-height: 22px; }

  .features { position: absolute; left: 226px; top: 356px; width: 974px; height: 256px; display: flex; }
  .feature { height: 100%; padding: 25px 28px 0 31px; border-left: 1px solid var(--border); }
  .feature:nth-child(1) { width: 324px; background: var(--panel); }
  .feature:nth-child(2) { width: 326px; background: var(--white); padding-left: 30px; }
  .feature:nth-child(3) { width: 324px; background: var(--panel); border-left: none; padding-left: 33px; }
  .feature h2 { font-family: "Montserrat", Arial, sans-serif; font-weight: 500; font-size: 14.4px; color: var(--orange); margin-bottom: 22px; }
  .feature p { font-size: 9.9px; line-height: 18px; color: var(--text); }
</style>
</head>
<body>
<div class="page">
  <aside class="sidebar">
    <div class="brand-name">Halden Event Management</div>
    <ul class="main-nav">
      <li><span class="nav-title">HOME</span><span class="nav-sub">Halden Event Management</span></li>
      <li><span class="nav-title">ABOUT</span><span class="nav-sub">Me and My Experiences</span></li>
      <li><span class="nav-title">SERVICES</span><span class="nav-sub">What I can Offer</span></li>
      <li><span class="nav-title">CONSULTING</span><span class="nav-sub">Giving you best Advice</span></li>
      <li><span class="nav-title">TESTIMONIALS</span><span class="nav-sub">What they Say</span></li>
      <li><span class="nav-title">BLOGS</span><span class="nav-sub">Whats Happening</span></li>
      <li><span class="nav-title">CONTACT</span><span class="nav-sub">Let's Talk</span></li>
    </ul>
    <div class="social-bar">
      <span class="social-dot" style="left:34px" aria-label="Social link"></span>
      <span class="social-dot" style="left:96px" aria-label="Social link"></span>
      <span class="social-dot" style="left:170px" aria-label="Social link"></span>
    </div>
  </aside>

  <header class="hero" role="img" aria-label="Black and white portrait of the event planner smiling, set against angled glass office architecture">
    <div class="hero-title">
      <h1>ABOUT</h1>
      <p>HALDEN EVENT MANAGEMENT</p>
    </div>
  </header>

  <section class="features">
    <article class="feature">
      <h2>What I do</h2>
      <p>Lorem ipsum dolor sit amet, consectetur adipiscing elit, sed do eiusmod tempor incididunt ut labore et dolore magna aliqua. Ut enim ad minim veniam, quis nostrud exercitation ullamco laboris nisi ut aliquip ex ea commodo consequat. Duis aute irure dolor in reprehenderit in voluptate velit esse cillum dolore eu fugiat nulla pariatur. Excepteur sint occaecat cupidatat non proident, sunt in culpa qui officia deserunt mollit anim id est laborum.</p>
    </article>
    <article class="feature">
      <h2>Why choose me</h2>
      <p>Sed ut perspiciatis unde omnis iste natus error sit voluptatem accusantium doloremque laudantium, totam rem aperiam, eaque ipsa quae ab illo inventore veritatis et quasi architecto beatae vitae dicta sunt explicabo. Nemo enim ipsam voluptatem quia voluptas sit aspernatur aut odit aut fugit, sed quia consequuntur magni dolores eos qui ratione voluptatem sequi nesciunt. Neque porro quisquam est, qui dolorem ipsum quia dolor sit amet,.</p>
    </article>
    <article class="feature">
      <h2>Where can you find me</h2>
      <p>Lorem ipsum dolor sit amet, consectetur adipiscing elit, sed do eiusmod tempor incididunt ut labore et dolore magna aliqua. Ut enim ad minim veniam, quis nostrud exercitation ullamco laboris nisi ut aliquip ex ea commodo consequat. Duis aute irure dolor in reprehenderit in voluptate velit esse cillum dolore eu fugiat nulla pariatur. Excepteur sint occaecat cupidatat non proident, sunt in culpa qui officia deserunt mollit anim id est laborum.</p>
    </article>
  </section>
</div>
</body>
</html>
```